Bref créative
Stationery - Business Card / Letterhead
For Public Adjusting Company
Professional
Doran T. Whitcombe
Sr. Public Adjuster
58 W. Alder St.
Suite 612
Harlow Bay, NY 11492
doran@trclaimpro.com
www.trclaimpro.com
On the front I want our logo with the shadow on the bottom
On the back I would like you to incorporate a little creative usage of either the shield/lighthouse logo and all of my information
This logo should be used as the front as it has the bottom shadow which for some reason is not showing up on the other logos
the business card front will be high gloss finish
Also the fax number should be 516.843.9075 not 829. there is no where else for me to edit that once the project is uploaded

```html
<!DOCTYPE html>
<html lang="en">
<head>
<meta charset="utf-8">
<title>TR Claim Advisors – Business Card</title>
<link href="https://fonts.googleapis.com/css2?family=Crimson+Text:wght@400;600&display=swap" rel="stylesheet">
<style>
  :root {
    --bg: #ece9e5;
    --card-white: #ffffff;
    --brand-red: #c8161d;
    --brand-red-dark: #8f0d12;
    --brand-navy: #1f4f8f;
    --text-gray: #555555;
    --text-dark: #2b2b2b;
  }
  html, body {
    margin: 0;
    padding: 0;
    width: 1200px;
    height: 713px;
    overflow: hidden;
    background: var(--bg);
    font-family: "Crimson Text", Georgia, serif;
  }
  .stage {
    width: 1200px;
    height: 713px;
    display: flex;
    align-items: center;
    justify-content: center;
    gap: 60px;
  }
  .card {
    position: relative;
    width: 525px;
    height: 300px;
    border-radius: 14px;
    box-shadow: 0 6px 18px rgba(0,0,0,0.18);
    overflow: hidden;
  }
  /* Front */
  .card--front { background: var(--card-white); }
  .card__edge-tab {
    position: absolute;
    left: 0;
    top: 180px;
    width: 8px;
    height: 56px;
    background: var(--brand-red);
  }
  .holder {
    position: absolute;
    left: 40px;
    top: 64px;
  }
  .holder__name {
    margin: 0;
    font-size: 22px;
    font-weight: 600;
    color: var(--brand-red);
  }
  .holder__title {
    margin: 2px 0 0 18px;
    font-size: 12px;
    color: var(--text-gray);
  }
  .contact {
    position: absolute;
    left: 40px;
    top: 170px;
    font-size: 11.5px;
    line-height: 1.45;
    color: var(--text-dark);
  }
  .contact p { margin: 0; }
  .contact__label { color: var(--brand-red); }
  .contact__web { color: var(--brand-red); font-weight: 600; }
  .brand {
    position: absolute;
    right: 36px;
    top: 96px;
    display: flex;
    align-items: center;
    gap: 10px;
  }
  .brand__mark {
    width: 38px;
    height: 38px;
    background: var(--brand-navy);
  }
  .brand__name {
    font-size: 19px;
    font-weight: 600;
    letter-spacing: 1px;
    text-transform: uppercase;
    color: var(--brand-navy);
    line-height: 1.05;
  }
  /* Back */
  .card--back {
    background: radial-gradient(ellipse at 50% 40%, var(--brand-red) 0%, #b3121a 55%, var(--brand-red-dark) 100%);
    display: flex;
    align-items: center;
    justify-content: center;
  }
  .brand--reverse {
    position: static;
    flex-direction: column;
    gap: 12px;
  }
  .brand--reverse .brand__mark {
    width: 52px;
    height: 52px;
    background: var(--card-white);
  }
  .brand--reverse .brand__name {
    color: var(--card-white);
    text-align: center;
  }
</style>
</head>
<body>
  <main class="stage">
    <section class="card card--front" aria-label="Card front">
      <div class="card__edge-tab"></div>
      <div class="holder">
        <h1 class="holder__name">Doran T. Whitcombe</h1>
        <p class="holder__title">Sr. Public Adjuster</p>
      </div>
      <div class="contact">
        <p>58 W. Alder St. Suite 612 Harlow Bay, NY 11492</p>
        <p><span class="contact__label">Tel</span> 516.843.9070 <span class="contact__label">Toll Free</span> 800.843.9071</p>
        <p><span class="contact__label">Fax</span> 516.843.9075</p>
        <p>doran@trclaimpro.com</p>
        <p class="contact__web">www.trclaimpro.com</p>
      </div>
      <div class="brand">
        <div class="brand__mark"></div>
        <div class="brand__name">TR Claim<br>Advisors</div>
      </div>
    </section>

    <section class="card card--back" aria-label="Card back">
      <div class="brand brand--reverse">
        <div class="brand__mark"></div>
        <div class="brand__name">TR Claim Advisors</div>
      </div>
    </section>
  </main>
</body>
</html>
```